Logo/ business card idea for a weld inspection/ nondestructive testing LLC

I have just started an LLC (my first) for weld inspection and non-destructive testing. I am the president and only member of this company. It is a very niche industry and word of mouth is basically the only advertisement needed to get you the next job. I will offer magnetic particle, dye penetrant, ultrasonic, and visual testing for the non-destructive services. X-ray is a form of non-destructive testing that I spent a few years doing but to costly for me at this time. All pipelines under the ground are welded, visually inspected and x-ray by someone just like me. All new building construction, any type of nuclear plant , pressure vessel, ect. , the welds are inspected by someone like me. Its is every increasing also with safety concerns. People are living right next to this stuff!!I will be the guy that fabrication shops or construction companies call to give the final OK that the welds are satisfactory after inspection to a certain code or standard. The designers have all the freedom they wish but I have attached a PDF with greater explanations and color ideas. I want raised glossy print on the front of the card and the necessary info. The back will not have raised print and serve more as a brief resume listing the certifications I have. The company only cares about the certifications and ultimately my signature. I want to make the front of the car into a fridge magnet to pass out with the card also. Something that is appealing to hang up instead of getting lost in someones wallet. The final design………. should be classic and stand the test of time. It should communicate precision and accuracy as well as incorporate the sound beam you will find in the PDF I’ve attached.Thanks and have a great day,Dwayne

Target Market(s)

Adult males in english speaking countries that handle welding and/or construction duties. Most of the time under heavy time constraints and deadlines. Ages 30-60

Industry/Entity Type

Construction

Contact Information for Business Card

Halvern Inspection Services, LLC
Dwayne Halvern
Ithaca, MI
989-517-2438
halv7dw@mailtrove.net

Font styles to use
Other font styles liked:
• designers choice

Requirements
Nice to have
• The logo on the front can completely encase the Halvern, be segmented incorporating the Halvern, or next to it. There can also be a couple of “flaws” (the red, blue and yellow in some of the pictures attached in the PDF) in the sound beam spread.

```html
<!DOCTYPE html>
<html lang="en">
<head>
<meta charset="utf-8">
<title>Halvern Inspection Services, LLC — Business Card</title>
<link href="https://fonts.googleapis.com/css2?family=Quicksand:wght@400;500;700&display=swap" rel="stylesheet">
<style>
  :root {
    --canvas: #e6e8ea;
    --brand-blue: #1ea6d8;
    --brand-blue-deep: #1590c2;
    --brand-blue-light: #5cc3ea;
    --card-white: #ffffff;
    --ink-white: #ffffff;
    --icon-hex: #8fb6cc;
    --shadow: rgba(20, 30, 40, 0.18);
  }
  * { box-sizing: border-box; margin: 0; padding: 0; }
  html, body {
    width: 1200px; height: 1000px; overflow: hidden;
    background: var(--canvas);
    font-family: "Quicksand", "Century Gothic", sans-serif;
  }
  .stage {
    position: relative; width: 1200px; height: 1000px;
    display: flex; flex-direction: column; align-items: center; justify-content: center; gap: 56px;
  }
  .card {
    position: relative; width: 640px; height: 366px; overflow: hidden;
    box-shadow: 0 10px 30px var(--shadow);
  }
  .card-shapes { position: absolute; inset: 0; width: 100%; height: 100%; }

  /* Back: certifications */
  .card--back { background: var(--card-white); color: var(--brand-blue); }
  .wordmark { position: absolute; font-weight: 500; line-height: 1; }
  .wordmark__name { display: block; letter-spacing: 0.02em; }
  .wordmark__sub { display: block; }
  .card--back .wordmark { left: 44px; top: 118px; color: var(--brand-blue); }
  .card--back .wordmark__name { font-size: 56px; }
  .card--back .wordmark__sub { font-size: 23px; margin-top: 4px; margin-left: 4px; }

  .cert-list {
    position: absolute; left: 262px; top: 200px; list-style: none;
    font-size: 18px; font-weight: 500; line-height: 1.3;
  }
  .cert-list li { position: relative; padding-left: 22px; }
  .cert-list li::before {
    content: ""; position: absolute; left: 0; top: 7px;
    width: 10px; height: 10px; border-radius: 50%; background: var(--brand-blue);
  }
  .cert-list .cert-sub { display: block; padding-left: 82px; }

  /* Front: contact */
  .card--front {
    background: linear-gradient(120deg, var(--brand-blue-deep) 0%, var(--brand-blue) 45%, var(--brand-blue-light) 100%);
    color: var(--ink-white);
  }
  .card--front .wordmark { left: 64px; top: 104px; color: var(--ink-white); }
  .card--front .wordmark__name { font-size: 50px; }
  .card--front .wordmark__sub { font-size: 20px; margin-top: 4px; margin-left: 3px; }

  .contact { position: absolute; left: 64px; top: 218px; }
  .contact__name { font-size: 22px; font-weight: 700; margin-bottom: 12px; }
  .contact__row { display: flex; align-items: center; gap: 14px; font-size: 19px; font-weight: 500; height: 40px; }
  .contact__icon { width: 30px; height: 30px; flex: none; }
</style>
</head>
<body>
<main class="stage">

  <section class="card card--back" aria-label="Card back: certifications">
    <svg class="card-shapes" viewBox="0 0 640 366" preserveAspectRatio="none" aria-hidden="true">
      <polygon points="360,0 640,0 640,78 600,78 640,40 640,0" fill="var(--brand-blue)"/>
      <polygon points="350,0 640,0 640,70" fill="var(--brand-blue)"/>
      <polygon points="0,262 0,366 300,366" fill="var(--brand-blue)"/>
      <polygon points="300,366 0,262 0,258 308,366" fill="#d9dde0"/>
    </svg>
    <h2 class="wordmark">
      <span class="wordmark__name">HALVERN</span>
      <span class="wordmark__sub">Inspection Services, LLC</span>
    </h2>
    <ul class="cert-list">
      <li>NWA Certified Welding Inspector</li>
      <li>NWA Certified Radiographic Interpreter</li>
      <li>NWA Certified Welding Educator</li>
      <li>Level II - Ultrasonic Testing
        <span class="cert-sub">Magnetic Particle Testing</span>
        <span class="cert-sub">Liquid Penetrant Testing</span>
      </li>
    </ul>
  </section>

  <section class="card card--front" aria-label="Card front: contact details">
    <h1 class="wordmark">
      <span class="wordmark__name">HALVERN</span>
      <span class="wordmark__sub">Inspection Services, LLC</span>
    </h1>
    <div class="contact">
      <p class="contact__name">Dwayne Halvern</p>
      <p class="contact__row">
        <svg class="contact__icon" viewBox="0 0 30 30" aria-hidden="true">
          <polygon points="15,1 27,8 27,22 15,29 3,22 3,8" fill="var(--icon-hex)"/>
          <path d="M11 9 l3 0 l1 4 l-2 1 q1 3 4 4 l1 -2 l4 1 l0 3 q-9 1 -11 -11z" fill="#fff"/>
        </svg>
        <span>989-517-2438</span>
      </p>
      <p class="contact__row">
        <svg class="contact__icon" viewBox="0 0 30 30" aria-hidden="true">
          <polygon points="15,1 27,8 27,22 15,29 3,22 3,8" fill="var(--icon-hex)"/>
          <rect x="8" y="10" width="14" height="10" fill="#fff"/>
          <path d="M8 10 l7 6 l7 -6" fill="none" stroke="var(--icon-hex)" stroke-width="1.4"/>
        </svg>
        <span>halv7dw@mailtrove.net</span>
      </p>
    </div>
  </section>

</main>
</body>
</html>
```